Travel Consultant Business Card

Hello.. New travel consultant looking seeking a business card that incorporates my new logo. I specialize in cruises but also want to imply land vacation. I am very open to any design and font concepts. I'm looking for a very upbeat modern design that reflects cruise and land vacations. Bright vibrant colors

Target Market(s)

Cruise and Land Vacationers

Industry/Entity Type

Travel Agent

Contact Information for Business Card

I am very open to any design and font concepts. I'm looking for a very upbeat modern design that reflects cruise and land vacations. Bright vibrant colors

Colors

Designer to choose colors to be used in the design.

Requirements
Must have
• Company Name: PineRidge Journeys---New logo uploaded to be included in design
• My Name: Danielle Marchetti-Travel Consultant
• Phone Number: (555) 418-7093
• E-Mail Address: pineridgejourneys@mailbox-example.com
• Website: www.pineridgejourneys-example.com
Nice to have
• My tag line is …..Here to Get You There

```html
<!DOCTYPE html>
<html lang="en">
<head>
<meta charset="utf-8">
<title>PineRidge Journeys – Business Card</title>
<link href="https://fonts.googleapis.com/css2?family=Roboto:wght@400;500;700&family=Roboto+Condensed:wght@700&display=swap" rel="stylesheet">
<style>
  :root {
    --brand-blue: #045cb0;
    --accent-blue: #16a9e8;
    --card-white: #ffffff;
    --backdrop: #e4e4e4;
    --ink-light: #ffffff;
  }
  * { margin: 0; padding: 0; box-sizing: border-box; }
  html, body {
    width: 1125px; height: 1200px; overflow: hidden;
    background: var(--backdrop);
    font-family: "Roboto", Arial, sans-serif;
  }
  .canvas { position: relative; width: 1125px; height: 1200px; }
  .card {
    position: absolute; left: 166px; width: 800px; height: 456px;
    border-radius: 24px; overflow: hidden;
  }
  .card--front { top: 103px; background: var(--card-white); }
  .card--back { top: 619px; background: var(--brand-blue); }
  .front-wave { position: absolute; inset: 0; width: 800px; height: 456px; }
  .holder { position: absolute; left: 42px; top: 102px; color: var(--ink-light); }
  .holder-name {
    font-family: "Roboto Condensed", "Arial Narrow", sans-serif;
    font-weight: 700; font-size: 29px; letter-spacing: 0.2px; line-height: 1;
  }
  .holder-title { font-size: 20px; margin-top: 6px; }
  .contact-list { position: absolute; left: 43px; top: 274px; list-style: none; color: var(--ink-light); }
  .contact-item { display: flex; align-items: center; font-size: 16.5px; height: 26px; white-space: nowrap; }
  .contact-icon { width: 17px; height: 17px; margin-right: 11px; flex: none; fill: var(--ink-light); }
  .brand-name {
    position: absolute; left: 430px; width: 340px; top: 196px;
    text-align: center; font-weight: 700; font-size: 33px; color: var(--brand-blue);
    line-height: 1.15;
  }
  .back-brand {
    position: absolute; left: 58px; top: 316px;
    font-weight: 700; font-size: 44px; color: var(--ink-light); line-height: 1;
  }
  .back-web {
    position: absolute; left: 68px; top: 383px;
    font-size: 18px; letter-spacing: 2.6px; color: var(--ink-light);
  }
</style>
</head>
<body>
<main class="canvas">
  <section class="card card--front" aria-label="Card front">
    <svg class="front-wave" viewBox="0 0 800 456" aria-hidden="true">
      <path d="M0 0 H406 C360 60 372 170 398 250 C420 330 412 400 372 456 H0 Z" fill="var(--brand-blue)"/>
      <path d="M406 0 C360 60 372 170 398 250 C420 330 412 400 372 456 H382 C424 400 432 330 410 250 C384 170 372 60 406 0 Z" fill="var(--accent-blue)"/>
    </svg>
    <div class="holder">
      <h1 class="holder-name">DANIELLE MARCHETTI</h1>
      <p class="holder-title">Travel Consultant</p>
    </div>
    <ul class="contact-list">
      <li class="contact-item">
        <svg class="contact-icon" viewBox="0 0 24 24"><path d="M6.6 10.8a15.1 15.1 0 0 0 6.6 6.6l2.2-2.2c.3-.3.7-.4 1-.2 1.1.4 2.3.6 3.6.6.6 0 1 .4 1 1V20c0 .6-.4 1-1 1C10.6 21 3 13.4 3 4c0-.6.4-1 1-1h3.5c.6 0 1 .4 1 1 0 1.2.2 2.4.6 3.6.1.3 0 .7-.2 1z"/></svg>
        (555) 418-7093
      </li>
      <li class="contact-item">
        <svg class="contact-icon" viewBox="0 0 24 24"><path d="M3 7l9 6 9-6v11H3z"/><path d="M3 5h18l-9 6z"/></svg>
        pineridgejourneys@mailbox-example.com
      </li>
      <li class="contact-item">
        <svg class="contact-icon" viewBox="0 0 24 24"><circle cx="12" cy="12" r="9" fill="none" stroke="#fff" stroke-width="2"/><path d="M12 3c-3 3-3 15 0 18M12 3c3 3 3 15 0 18M3.5 9h17M3.5 15h17" fill="none" stroke="#fff" stroke-width="1.6"/></svg>
        www.pineridgejourneys-example.com
      </li>
    </ul>
    <p class="brand-name">PineRidge Journeys</p>
  </section>

  <section class="card card--back" aria-label="Card back">
    <p class="back-brand">PineRidge Journeys</p>
    <p class="back-web">www.pineridgejourneys-example.com</p>
  </section>
</main>
</body>
</html>
```